political campaign lawn sign - Governor's Council in Massachuesetts

We are looking for a political lawn sign. We are running a campaign for Governor's Council in Massachusetts. This sign will be on the lawn of homes and businesses so people driving by will see it. It needs to be simple and bold. The last name is long so maybe it could say vote for Marty and then Kolbeck will be big a bold on the next line??
We need it to say:
Vote for Martin Kolbeck
Governor's Council.

Target Market(s)

local residents

Industry/Entity Type

Politcal Campaign

Font styles to use
Sans Serif
Other font styles liked:
• not sure what font but a modern looking one such as Helvetica, Arial, Sans Seri, sharp sans..

Colors
0054AA
0677BA
7BADD7
CADEEF
E8F1F8
00AB8E
00BBA5
67D7C9
C6EFE9
E9F9F6
FFF300
FFF600
FEFA6F
FFFEC7
FFFEE8

Requirements
Must have
• My name written out with a Capital D and R but lower case for every other letter so its Marty Kolbeck
Nice to have
• modern font , the Colors of the lawn sign should have Blue, Yellow and White something bold that will stand out
Should not have
• any maps of Massachusetts

```html
<!DOCTYPE html>
<html lang="en">
<head>
<meta charset="utf-8">
<title>Vote for Marty Kolbeck – Governor's Council Lawn Sign</title>
<link rel="stylesheet" href="https://fonts.googleapis.com/css2?family=Outfit:wght@600;700;800&display=swap">
<style>
  :root {
    --sign-blue: #0054AA;
    --sign-white: #FFFFFF;
  }
  html, body {
    margin: 0;
    padding: 0;
    width: 1200px;
    height: 900px;
    overflow: hidden;
    background: var(--sign-blue);
  }
  .lawn-sign {
    display: block;
    width: 1200px;
    height: 900px;
  }
  .sign-field { fill: var(--sign-blue); }
  .sign-band { fill: var(--sign-white); }
  .vote-for {
    fill: var(--sign-blue);
    font-family: "Outfit", sans-serif;
    font-weight: 800;
    font-size: 104px;
  }
  .candidate-name {
    fill: var(--sign-white);
    font-family: "Outfit", sans-serif;
    font-weight: 700;
    font-size: 262px;
    letter-spacing: -4px;
  }
  .office-title {
    fill: var(--sign-blue);
    font-family: "Outfit", sans-serif;
    font-weight: 700;
    font-size: 82px;
  }
</style>
</head>
<body>
<svg class="lawn-sign" viewBox="0 0 1200 900" xmlns="http://www.w3.org/2000/svg" role="img" aria-label="Vote for Marty Kolbeck, Governer's Council">
  <rect class="sign-field" x="0" y="0" width="1200" height="900"/>

  <!-- diagonal banner -->
  <polygon class="sign-band" points="362,0 603,0 0,447 0,268"/>
  <text class="vote-for" x="0" y="0" text-anchor="middle" textLength="440" lengthAdjust="spacingAndGlyphs"
        transform="translate(232,212) rotate(-36.5)">Vote for</text>

  <!-- candidate name -->
  <text class="candidate-name" x="1149" y="409" text-anchor="end">Marty</text>
  <text class="candidate-name" x="62" y="632">Kolbeck</text>

  <!-- office band -->
  <rect class="sign-band" x="0" y="703" width="1200" height="106"/>
  <text class="office-title" x="101" y="787" textLength="1006" lengthAdjust="spacing">GOVERNER’S COUNCIL</text>
</svg>
</body>
</html>
```